Flyer-Design für Unkrautbekämpfung
Sehr gute und nette Zusammenarbeit. Auch auf Änderungswünsche nach Beendigung der Contest-Phase wurde schnell eingegangen. Gerne wieder, sehr zu empfehlen!
Zielgruppe
Unkrautbekämpfung mit dem Heißwasser-Schaum-System. In Eigenleistung und Vermietung des Geräts.
Zielgruppe: Privatleute mit eigenem Grundstück, Landwirte, kleine Geschäfte (Restaurants, Läden mit Parkplatz etc.)
Aufgabenstellung
Link zur Website: www.beetglanz-service.net
Der Kreativität sind keine Grenzen gesetzt.
Bitte Vorder- und Rückseite designen. Auf der Rückseite können hauptsächlich Kontaktinformationen sein.

```html
<!DOCTYPE html>
<html lang="de">
<head>
<meta charset="utf-8">
<title>GKS Flyer – Vorder- und Rückseite</title>
<link href="https://fonts.googleapis.com/css2?family=Source+Sans+3:wght@400;600;700&display=swap" rel="stylesheet">
<style>
  :root {
    --green: #2f7a3b;
    --green-dark: #25632f;
    --navy: #1f2a55;
    --paper: #ffffff;
    --backdrop: #eef0ee;
    --ink: #1c1c1c;
  }
  * { box-sizing: border-box; margin: 0; padding: 0; }
  html, body { width: 1200px; height: 846px; overflow: hidden; }
  body {
    background: var(--backdrop);
    font-family: "Source Sans 3", "Helvetica Neue", Arial, sans-serif;
    position: relative;
  }
  .flyer {
    position: absolute;
    top: 70px;
    width: 500px;
    height: 707px;
    background: var(--paper);
    overflow: hidden;
    box-shadow: 0 6px 18px rgba(0,0,0,.12);
  }
  .flyer--front { left: 70px; }
  .flyer--back { left: 630px; }

  .brand {
    position: absolute;
    top: 38px;
    left: 50px;
    display: flex;
    align-items: center;
    gap: 12px;
    color: var(--green);
  }
  .brand__square { width: 48px; height: 48px; background: var(--green); }
  .brand__name { font-size: 24px; font-weight: 400; line-height: 1; }
  .brand__tagline { font-size: 15px; font-weight: 400; color: var(--green); margin-top: 4px; }

  .placeholder { position: absolute; }
  .hero-photo {
    left: 22px; top: 108px; width: 396px; height: 523px;
    background: linear-gradient(180deg, #7c9b63 0%, #6d7f6a 35%, #7a7d86 65%, #5e6170 100%);
  }
  .spray-illustration--front {
    right: 0; top: 18px; width: 170px; height: 160px;
    background: radial-gradient(circle at 45% 45%, #cfe6cf 0%, #f4f8f4 70%, #ffffff 100%);
  }

  .banner {
    position: absolute;
    background: var(--green);
    color: #fff;
    font-weight: 700;
    text-align: center;
    white-space: nowrap;
  }
  .headline {
    font-size: 33px; line-height: 1;
    display: flex; align-items: center; justify-content: center;
  }
  .headline--line1 { left: 78px; top: 238px; width: 330px; height: 70px; }
  .headline--line2 { left: 142px; top: 306px; width: 180px; height: 58px; }

  .subline {
    position: absolute;
    left: 30px; top: 378px; width: 400px;
    text-align: center; color: #fff;
    font-size: 19px; font-weight: 700; line-height: 1.2;
    text-shadow: 0 1px 3px rgba(0,0,0,.55);
  }

  .benefit {
    left: 0; height: 44px;
    display: flex; align-items: center; gap: 10px;
    padding-left: 20px;
    font-size: 18px; font-weight: 600;
  }
  .benefit svg { width: 20px; height: 20px; flex: none; }
  .benefit--1 { top: 443px; width: 276px; }
  .benefit--2 { top: 508px; width: 343px; }
  .benefit--3 { top: 570px; width: 246px; }

  .footer-band {
    position: absolute; left: 0; bottom: 8px; width: 100%; height: 46px;
    background: var(--green); color: #fff;
    display: flex; align-items: center; justify-content: center;
  }
  .footer-band--claims { font-size: 13px; font-weight: 600; }
  .footer-band--web { font-size: 17px; font-weight: 700; letter-spacing: .3px; }

  .comparison-photo { top: 119px; height: 306px; }
  .comparison-photo--before {
    left: 0; width: 250px;
    background: linear-gradient(180deg, #5f8c4a 0%, #7da060 45%, #8a9a83 100%);
  }
  .comparison-photo--after {
    left: 250px; width: 250px;
    background: linear-gradient(180deg, #4f7e3e 0%, #8fa27b 40%, #b6b3ad 100%);
  }
  .photo-label {
    top: 140px; height: 38px;
    font-size: 17px; font-weight: 600;
    display: flex; align-items: center; justify-content: center;
  }
  .photo-label--before { left: 18px; width: 124px; }
  .photo-label--after { left: 265px; width: 124px; }

  .cta--line1 { left: 102px; top: 386px; width: 254px; height: 66px; }
  .cta--line2 { left: 135px; top: 450px; width: 182px; height: 60px; }

  .spray-illustration--back {
    left: 330px; top: 470px; width: 170px; height: 170px;
    background: radial-gradient(circle at 40% 50%, #cfe6cf 0%, #f4f8f4 70%, #ffffff 100%);
  }

  .contact {
    position: absolute; left: 60px; top: 535px;
    color: var(--ink); font-size: 15px; line-height: 1.3;
  }
  .contact__company { font-weight: 700; font-size: 15px; }
  .contact__lines { margin-top: 14px; }
  .contact__row { display: flex; align-items: center; gap: 7px; }
  .contact__row svg { width: 13px; height: 13px; flex: none; }
</style>
</head>
<body>

<article class="flyer flyer--front">
  <div class="placeholder hero-photo" role="img" aria-label="Foto: Pflasterweg mit Unkraut entlang einer Hauswand und Rasenkante"></div>
  <div class="placeholder spray-illustration--front" role="img" aria-label="Illustration: Person sprüht Heißwasserschaum auf grünes Unkraut"></div>

  <header class="brand">
    <span class="brand__square"></span>
    <div>
      <div class="brand__name">GKS</div>
      <div class="brand__tagline">Biologische Unkrautvernichtung</div>
    </div>
  </header>

  <h1 class="banner headline headline--line1">Unkraut ohne Gift</h1>
  <div class="banner headline headline--line2">im Griff</div>

  <p class="subline">Flächenpflege mit dem Heißwasser-/<br>Ökoschaum-Verfahren</p>

  <div class="banner benefit benefit--1">
    <svg viewBox="0 0 20 20" fill="none" stroke="#fff" stroke-width="1.4" stroke-linecap="round"><path d="M10 18V8"/><path d="M10 11C6 11 4 8 4 4c4 0 6 3 6 7z"/><path d="M10 9c0-4 2-6 6-6 0 4-2 6-6 6z"/></svg>
    Sofort sichtbares Ergebnis!
  </div>
  <div class="banner benefit benefit--2">
    <svg viewBox="0 0 20 20" fill="none" stroke="#fff" stroke-width="1.4" stroke-linecap="round"><path d="M10 18V8"/><path d="M10 11C6 11 4 8 4 4c4 0 6 3 6 7z"/><path d="M10 9c0-4 2-6 6-6 0 4-2 6-6 6z"/></svg>
    Geeignet für fast alle Untergründe
  </div>
  <div class="banner benefit benefit--3">
    <svg viewBox="0 0 20 20" fill="none" stroke="#fff" stroke-width="1.4" stroke-linecap="round"><path d="M10 18V8"/><path d="M10 11C6 11 4 8 4 4c4 0 6 3 6 7z"/><path d="M10 9c0-4 2-6 6-6 0 4-2 6-6 6z"/></svg>
    Wirtschaftlich günstig
  </div>

  <footer class="footer-band footer-band--claims">100% biologisch abbaubar • umweltfreundlich • nicht gesundheitsschädlich</footer>
</article>

<article class="flyer flyer--back">
  <header class="brand">
    <span class="brand__square"></span>
    <div>
      <div class="brand__name">GKS</div>
      <div class="brand__tagline">Biologische Unkrautvernichtung</div>
    </div>
  </header>

  <div class="placeholder comparison-photo comparison-photo--before" role="img" aria-label="Foto vorher: Tischtennisplatte auf verunkrauteter Pflasterfläche im Park"></div>
  <div class="placeholder comparison-photo comparison-photo--after" role="img" aria-label="Foto nachher: Tischtennisplatte auf sauberer Pflasterfläche im Park"></div>

  <div class="banner photo-label photo-label--before">vorher</div>
  <div class="banner photo-label photo-label--after">nachher</div>

  <div class="placeholder spray-illustration--back" role="img" aria-label="Illustration: Person sprüht Heißwasserschaum auf grünes Unkraut"></div>

  <h2 class="banner headline cta--line1">Kontaktieren</h2>
  <div class="banner headline cta--line2">Sie uns!</div>

  <address class="contact" style="font-style:normal">
    <div class="contact__company">GKS - Biologische Unkrautvernichtung</div>
    <div>Lindenweg 12 • 31599 Kolbeck</div>
    <div class="contact__lines">
      <div class="contact__row">
        <svg viewBox="0 0 16 16" fill="#8a8a8a"><path d="M3.5 1.5l2.5 0 1 3.5-1.6 1.2a8 8 0 0 0 4.4 4.4L11 9l3.5 1v2.5c0 1-1 2-2 2A11 11 0 0 1 1.5 3.5c0-1 1-2 2-2z"/></svg>
        Tel: 05021/4470 • Mobil : 0171/3325914
      </div>
      <div class="contact__row">
        <svg viewBox="0 0 16 16" fill="none" stroke="#8a8a8a" stroke-width="1.6"><rect x="1.5" y="3.5" width="13" height="9"/><path d="M1.5 3.5l6.5 5 6.5-5"/></svg>
        info@beetglanz-service.net
      </div>
    </div>
  </address>

  <footer class="footer-band footer-band--web">www.beetglanz-service.net</footer>
</article>

</body>
</html>
```